New Year Resolution Infographic

We are a weight loss company that provides holistic, natural nutrition programs to consumers -- you can see our Web site at www.SlimBirch.com We need a simple infographic to be shared on social media and via email for New Year's day. The topic for the infographic is "how to set and keep your weight loss resolution". We've outlined 5 process steps for consumers to follow to assist with their weight loss resolutions, and we would like to depict this graphically.

Target Market(s)

Women age 35-65 who are planning to make a resolution to lose weight in the new year.

Industry/Entity Type

Health And Wellness

Font styles to use
Sans Serif

Colors
0392cd
9bcb3c

Requirements
Must have
• Initial graphic showing failure stats (see copy)
• Graphic showing process steps in making/keeping a resolution (see copy)
• SlimBirch Logo

```html
<!DOCTYPE html>
<html lang="en">
<head>
<meta charset="utf-8">
<title>SlimBirch – How to set &amp; reach your Weight Loss Resolution</title>
<link href="https://fonts.googleapis.com/css2?family=Mulish:wght@400;600;700;800;900&display=swap" rel="stylesheet">
<style>
  :root {
    --teal: #1fb3c9;
    --teal-band: #1a8aa3;
    --teal-dark: #178fa5;
    --teal-ring: #3cc3d6;
    --green: #8dc63f;
    --green-deep: #3aaa5c;
    --green-foot: #2e9e6a;
    --record: #ececec;
    --record-ring: #cfd0d0;
    --ink: #2b2b2b;
    --white: #ffffff;
  }
  * { box-sizing: border-box; margin: 0; padding: 0; }
  html, body { width: 849px; height: 1200px; overflow: hidden; }
  body { font-family: "Mulish", "Helvetica Neue", Arial, sans-serif; background: var(--white); }
  .sheet { position: relative; width: 849px; height: 1200px; overflow: hidden; background: var(--white); }

  .masthead {
    position: absolute; left: 0; top: 0; width: 849px; height: 318px;
    background: radial-gradient(ellipse at 40% 40%, #f4f4f4 0%, #e2e3e3 60%, #d6d7d7 100%);
  }
  .brand { position: absolute; left: 52px; top: 120px; display: flex; align-items: center; gap: 12px; }
  .brand-dot { width: 34px; height: 34px; border-radius: 50%; background: var(--green); }
  .brand-name { font-size: 44px; font-weight: 600; color: var(--teal); letter-spacing: 0.5px; line-height: 1; }

  .headline { position: absolute; left: 418px; top: 40px; width: 420px; }
  .headline .lead { font-size: 34px; font-weight: 400; color: var(--teal); line-height: 1; white-space: nowrap; }
  .headline .topic { font-size: 35px; font-weight: 800; color: var(--teal); line-height: 1; margin-top: 4px; }
  .headline .word { font-size: 55px; font-weight: 900; color: var(--teal); line-height: 1; margin-top: 10px; letter-spacing: -1px; }
  .headline .rank { position: absolute; left: 70px; top: 146px; width: 238px; text-align: right; font-size: 34px; color: var(--green-deep); line-height: 1.08; }
  .headline .numeral { position: absolute; left: 296px; top: 62px; font-size: 200px; font-weight: 900; color: var(--green); line-height: 1; }

  .stat-band { position: absolute; left: 0; top: 318px; width: 849px; height: 120px; background: var(--green); }
  .stat-band p { position: absolute; left: 37px; top: 26px; width: 346px; font-size: 13.6px; line-height: 1.42; color: var(--white); }
  .guide-band { position: absolute; left: 0; top: 438px; width: 849px; height: 150px; background: var(--teal-band); }
  .guide-band p { position: absolute; left: 36px; top: 24px; width: 320px; font-size: 20px; line-height: 1.25; color: var(--white); }

  .portrait {
    position: absolute; left: 0; top: 588px; width: 400px; height: 580px;
    background: linear-gradient(160deg, #f3f1ec 0%, #e8e0d0 45%, #b9c98a 70%, #d56a4a 100%);
  }

  .step {
    position: absolute; border-radius: 50%; display: flex; flex-direction: column;
    align-items: center; justify-content: center; text-align: center; color: var(--white);
  }
  .step svg { display: block; margin-bottom: 6px; }
  .step h2 { font-size: 18px; font-weight: 800; letter-spacing: 0.3px; margin-bottom: 3px; line-height: 1.25; }
  .step p { font-size: 13.4px; line-height: 1.27; }

  .step-replace { left: 516px; top: 512px; width: 280px; height: 280px; background: var(--teal-dark); border: 7px solid var(--teal); justify-content: flex-start; padding-top: 42px; z-index: 1; }
  .step-replace p { width: 228px; }
  .step-reflect { left: 584px; top: 296px; width: 256px; height: 256px; background: var(--teal); border: 7px solid var(--teal-band); z-index: 2; }
  .step-reflect p { width: 176px; }
  .step-resolve { left: 354px; top: 364px; width: 264px; height: 264px; background: var(--green); border: 7px solid var(--teal-band); z-index: 3; }
  .step-resolve p { width: 186px; }
  .step-reward { left: 356px; top: 700px; width: 264px; height: 264px; background: var(--teal); border: 7px solid var(--teal-ring); z-index: 4; }
  .step-reward p { width: 196px; }
  .step-record { left: 590px; top: 756px; width: 248px; height: 248px; background: var(--record); border: 8px solid var(--record-ring); color: var(--ink); z-index: 5; }
  .step-record p { width: 188px; }
  .step-record h2 { color: var(--ink); }

  .offers { position: absolute; left: 412px; top: 1020px; width: 410px; list-style: none; }
  .offers li { position: relative; padding-left: 22px; font-size: 14px; font-weight: 700; line-height: 1.36; color: var(--ink); margin-bottom: 10px; }
  .offers li svg { position: absolute; left: 0; top: 3px; }

  .web { position: absolute; left: 414px; top: 1116px; display: flex; align-items: center; gap: 12px; }
  .web-dot { width: 24px; height: 24px; border-radius: 50%; background: radial-gradient(circle at 35% 35%, #6d7a80, #1c2428); }
  .web span { font-size: 26px; letter-spacing: 6px; color: #444; }
  .web b { font-weight: 800; color: #333; }

  .footer-band { position: absolute; left: 0; top: 1168px; width: 849px; height: 32px; background: var(--green-foot); }
</style>
</head>
<body>
<div class="sheet">

  <header class="masthead">
    <div class="brand">
      <span class="brand-dot"></span>
      <span class="brand-name">SLIMBIRCH</span>
    </div>
    <div class="headline">
      <div class="lead">How to set &amp; reach your</div>
      <div class="topic">Weight Loss</div>
      <div class="word">Resolution</div>
      <div class="rank">Weight loss is<br>the #</div>
      <div class="numeral">1</div>
    </div>
  </header>

  <section class="stat-band">
    <p>New Year resolution, but we know that resolutions are very difficult to keep. <strong>While 45%</strong> of Americans make New Year resolutions, only 8% succeed in keeping those resolutions.</p>
  </section>
  <section class="guide-band">
    <p>Here is a quick guide to setting &amp; reaching your weight loss resolution this year.</p>
  </section>

  <div class="portrait" role="img" aria-label="Photo of a smiling woman in a black T-shirt surrounded by fresh fruit and vegetables"></div>

  <article class="step step-replace">
    <svg width="56" height="56" viewBox="0 0 64 64" fill="none" stroke="#fff" stroke-width="5" stroke-linecap="round">
      <path d="M14 36 A19 19 0 0 1 40 14" stroke-dasharray="8 5"/>
      <path d="M50 28 A19 19 0 0 1 24 50" stroke-dasharray="8 5"/>
      <path d="M36 8 L42 14 L35 19" />
      <path d="M28 56 L22 50 L29 45" />
    </svg>
    <h2>REPLACE</h2>
    <p>Clear out your pantry and stock up with only healthy foods. Then work to build new activity and eating habits that take the place of your current habits.</p>
  </article>

  <article class="step step-reflect">
    <svg width="74" height="60" viewBox="0 0 74 60" fill="#fff">
      <path d="M24 6 A18 10 0 0 1 52 6" fill="none" stroke="#fff" stroke-width="2.5"/>
      <path d="M22 2 L24 9 L29 4 Z"/>
      <path d="M6 20 L33 38 L6 56 Z"/>
      <path d="M68 20 L41 38 L68 56 Z"/>
      <rect x="36" y="18" width="2" height="40"/>
    </svg>
    <h2>REFLECT</h2>
    <p>Get clear on why the achievement of your resolution is important. You'll need to come back to this if you falter!</p>
  </article>

  <article class="step step-resolve">
    <svg width="60" height="60" viewBox="0 0 64 64" fill="none" stroke="#fff" stroke-width="4" stroke-linecap="round">
      <path d="M24 44 C24 36 18 34 18 26 A14 14 0 0 1 46 26 C46 34 40 36 40 44 Z"/>
      <path d="M25 50 H39 M27 56 H37"/>
      <path d="M32 2 V8 M10 10 L14 14 M54 10 L50 14 M2 28 H8 M56 28 H62"/>
    </svg>
    <h2>RESOLVE</h2>
    <p>Set a weight loss goal for the year that is realistic, then break this up into even shorter term goals of 30-60 days, with a specific diet and activity plan to guide you.</p>
  </article>

  <article class="step step-reward">
    <svg width="64" height="62" viewBox="0 0 64 62" fill="none" stroke="#fff" stroke-width="4" stroke-linejoin="round">
      <rect x="6" y="22" width="52" height="12"/>
      <rect x="10" y="34" width="44" height="24"/>
      <path d="M32 22 V58"/>
      <path d="M32 22 C24 6 12 10 18 18 C20 21 26 22 32 22 C38 22 44 21 46 18 C52 10 40 6 32 22 Z"/>
    </svg>
    <h2>REWARD</h2>
    <p>Rather than using unhealthy food as a reward or cheat, give yourself healthy or relaxing experiences-such a spa treatment or taking a new fitness class.</p>
  </article>

  <article class="step step-record">
    <svg width="72" height="56" viewBox="0 0 72 56">
      <rect x="2" y="6" width="68" height="48" rx="3" fill="var(--teal-dark)"/>
      <rect x="26" y="0" width="20" height="10" rx="2" fill="var(--teal-dark)"/>
      <rect x="8" y="14" width="24" height="32" fill="#fff"/>
      <circle cx="20" cy="26" r="6" fill="var(--teal-dark)"/>
      <path d="M10 44 C10 34 30 34 30 44 Z" fill="var(--teal-dark)"/>
      <rect x="38" y="16" width="26" height="4" fill="#fff"/>
      <rect x="38" y="26" width="26" height="4" fill="#fff"/>
      <rect x="38" y="36" width="26" height="4" fill="#fff"/>
    </svg>
    <h2>RECORD</h2>
    <p>Track your progress daily, tell your family and friends about your resolution to create more accountability, and recruit a partner to share your journey.</p>
  </article>

  <ul class="offers">
    <li><svg width="12" height="12" viewBox="0 0 12 12" fill="none" stroke="#1a8aa3" stroke-width="1.8"><path d="M1 6 L4.5 9.5 L11 2"/></svg>SlimBirch can help you achieve your weight loss resolution in the New Year.</li>
    <li><svg width="12" height="12" viewBox="0 0 12 12" fill="none" stroke="#1a8aa3" stroke-width="1.8"><path d="M1 6 L4.5 9.5 L11 2"/></svg>We invite you to learn more and contact us for a free consultation.</li>
  </ul>

  <div class="web">
    <span class="web-dot"></span>
    <span>www.<b>slimbirch</b>.com</span>
  </div>

  <div class="footer-band"></div>
</div>
</body>
</html>
```